Dale Winslow Drum Demo

My husband and I just moved to Nashville. Dale (my husband) is a drummer with 30 years of experience. We have a CD that we would like to promote with hope that he can get a gig doing what he loves. We would like your talented artists to create a CD cover and label. We are here to promote Dale, although we also think the rest of the band should be mentioned and recognized. I am going to put the names of the musicians as well as two pictures that can be used for the outside cover if necessary. On the inside of the cover I would like the band members mentioned as well as a little bio. about Dale.
Dale Winslow - drums and vocals
Mark Delvey - vocals
Rick Hanlon - bass
Pete Morant - lead guitar

Dale's bio
Born in Massachusetts
30 years experience
some drumming school
local band experience
music played: blues, classic rock, country, jazz, and alternative
influences: Carl Mesner, Lenny Vask, Glen Fosk, Walt Dusek
Great passion, feel, and desire for music....something which cannot be taught!!!

```html
<!DOCTYPE html>
<html lang="en">
<head>
<meta charset="utf-8">
<title>Dale Winslow – CD Inside Cover</title>
<link rel="stylesheet" href="https://fonts.googleapis.com/css2?family=Arimo:wght@700&display=swap">
<style>
  :root {
    --page: #ffffff;
    --ink: #ffffff;
    --night: #050505;
    --stage-dark: #1c1a1a;
    --stage-grey: #6e6a6a;
    --stage-light: #a9a6a6;
    --stage-red: #c40f0f;
    --stage-deep-red: #5e0606;
    --shadow: rgba(0, 0, 0, 0.75);
  }
  * { margin: 0; padding: 0; box-sizing: border-box; }
  html, body {
    width: 1200px;
    height: 1200px;
    overflow: hidden;
    background: var(--page);
  }
  .cover {
    position: absolute;
    left: 42px;
    top: 38px;
    width: 1125px;
    height: 1125px;
    overflow: hidden;
    background: var(--night);
    font-family: "Arimo", Arial, sans-serif;
    font-weight: 700;
    color: var(--ink);
    text-shadow: 1px 2px 3px var(--shadow);
  }
  .stage-photo {
    position: absolute;
    left: 0;
    top: 0;
    width: 1125px;
    height: 1039px;
    background:
      radial-gradient(ellipse 300px 330px at 730px 480px, rgba(196, 15, 15, 0.85), transparent 70%),
      radial-gradient(ellipse 240px 200px at 1000px 260px, rgba(150, 10, 10, 0.7), transparent 70%),
      radial-gradient(ellipse 260px 160px at 180px 160px, rgba(169, 166, 166, 0.7), transparent 70%),
      radial-gradient(ellipse 420px 260px at 560px 860px, rgba(94, 6, 6, 0.55), transparent 75%),
      linear-gradient(180deg, var(--stage-grey) 0%, #4a4646 35%, var(--stage-dark) 62%, #141212 100%);
  }
  .lineup {
    position: absolute;
    left: 70px;
    top: 418px;
    list-style: none;
    font-size: 26px;
    line-height: 43px;
  }
  .bio {
    position: absolute;
    right: 64px;
    top: 650px;
    text-align: right;
  }
  .bio-title {
    font-size: 33px;
    line-height: 44px;
    margin-bottom: 6px;
  }
  .bio-facts {
    list-style: none;
    font-size: 22px;
    line-height: 43.5px;
  }
</style>
</head>
<body>
  <main class="cover">
    <div class="stage-photo" role="img" aria-label="Photograph of a drum kit on a stage with cymbals, a microphone stand and an amplifier, in greyscale with red splashes"></div>

    <ul class="lineup">
      <li>Dale Winslow - drums and vocals</li>
      <li>Mark Delvey - vocals</li>
      <li>Rick Hanlon - bass</li>
      <li>Pete Morant - lead guitar</li>
    </ul>

    <section class="bio">
      <h2 class="bio-title">Dale's bio</h2>
      <ul class="bio-facts">
        <li>Born in Massachusetts</li>
        <li>30 years experience</li>
        <li>some drumming school</li>
        <li>local band experience</li>
        <li>music played: blues, classic rock, country, jazz, and alternative</li>
        <li>influences: Carl Mesner, Lenny Vask, Glen Fosk, Walt Dusek</li>
        <li>Great passion, feel, and desire for music....something which cannot be taught!!!</li>
      </ul>
    </section>
  </main>
</body>
</html>
```